Quorvex clinic business card - double sided for young clinic

I require business cards for my aesthetic clinic specialising in the below treatments. I would like the cards to be modern as my clinic base are young 22-35 years old. I require my logo on it and would like the edges to be rounded.

I have an aesthetic clinic specialising in :
Quorvex
Lip Enhancement
Chemical Peels
Facial Fillers
Non Surgical Face Lift

I would the cards to have the following information on them:
My logo - (in grey/silver)
address
Phone number
services

Colours :
White/grey/silver and red

a nice image on there, perhaps a set of lips as this is a main service i deliver

Company Name: PDA Address: 52 Farrowmere Road, 4 Brackwell High Street, KT9 4WQ Phone: 0208 794 2160 Website: www.penningtondoweaesthetics.co.uk

Target Market(s)

clinics 22-45 years old mainly female

Industry/Entity Type

Business

Contact Information for Business Card

as above

Requirements
Must have
• logo
• Address
• Email
• Phone number
• Services i offer
Nice to have
• images

```html
<!DOCTYPE html>
<html lang="en">
<head>
<meta charset="utf-8">
<title>Pennington Dowe Aesthetics – Business Card</title>
<link rel="stylesheet" href="https://fonts.googleapis.com/css2?family=Cinzel:wght@400;700&family=Open+Sans:wght@400;600;700&display=swap">
<style>
  :root {
    --bg: #e6e6e6;
    --red: #a8181f;
    --red-bright: #d8212b;
    --white: #ffffff;
    --silver-light: #f4f4f4;
    --silver: #cfcfcf;
    --silver-dark: #9a9a9a;
    --ink: #222222;
    --lip: #e2404a;
  }
  * { margin: 0; padding: 0; box-sizing: border-box; }
  html, body { width: 1200px; height: 1000px; overflow: hidden; }
  body {
    background: var(--bg);
    position: relative;
    font-family: "Open Sans", Arial, sans-serif;
  }
  .card {
    position: absolute;
    width: 510px;
    height: 310px;
    border-radius: 18px;
    overflow: hidden;
    top: 345px;
    box-shadow: 0 6px 18px rgba(0,0,0,0.18);
  }

  /* Contact side */
  .card--contact { left: 50px; background: var(--red); }
  .card--contact .wave {
    position: absolute; left: 0; top: 0; width: 100%; height: 100%;
  }
  .services {
    position: absolute; left: 34px; top: 22px;
    list-style: none;
    color: var(--white);
    font-size: 14px; line-height: 22px; letter-spacing: 0.3px;
    text-transform: uppercase;
  }
  .contact {
    position: absolute; right: 28px; bottom: 16px;
    text-align: right;
  }
  .contact__label {
    font-size: 10px; line-height: 13px; font-weight: 700; letter-spacing: 0.5px;
    color: var(--ink); text-transform: uppercase;
  }
  .contact__label--phone { font-weight: 400; }
  .contact__phone {
    font-size: 20px; line-height: 26px; font-weight: 700; color: var(--red-bright);
  }
  .contact__email, .contact__address {
    font-size: 13px; line-height: 18px; color: var(--red-bright);
  }
  .contact__email { margin-bottom: 2px; }

  /* Brand side */
  .card--brand {
    left: 640px;
    background: linear-gradient(135deg, var(--silver-light) 0%, var(--white) 40%, var(--silver) 100%);
  }
  .website {
    position: absolute; right: 26px; top: 22px;
    font-size: 14px; color: var(--red-bright); letter-spacing: 0.2px;
  }
  .lips-photo {
    position: absolute; left: 170px; top: 70px; width: 320px; height: 190px;
    border-radius: 50%;
    background: radial-gradient(ellipse at 50% 50%, var(--lip) 0%, #f07b80 38%, rgba(240,180,182,0.4) 62%, rgba(255,255,255,0) 75%);
  }
  .brand-mark {
    position: absolute; left: 300px; top: 122px;
    font-family: "Cinzel", Georgia, serif;
    font-size: 30px; font-weight: 700; color: var(--white);
    letter-spacing: 2px;
  }
  .brand-name {
    position: absolute; left: 36px; top: 186px;
    font-family: "Cinzel", Georgia, serif;
    color: var(--silver-dark);
    text-transform: uppercase;
  }
  .brand-name__first { font-size: 22px; letter-spacing: 6px; line-height: 28px; }
  .brand-name__second { font-size: 42px; font-weight: 700; letter-spacing: 7px; line-height: 48px; }
</style>
</head>
<body>

  <section class="card card--contact" aria-label="Contact side">
    <svg class="wave" viewBox="0 0 510 310" aria-hidden="true">
      <path d="M0 185 Q220 120 510 150 L510 310 L0 310 Z" fill="var(--white)"/>
      <path d="M0 198 Q220 134 510 163" fill="none" stroke="var(--red)" stroke-width="3"/>
    </svg>
    <ul class="services">
      <li>Quorvex</li>
      <li>Lip Enhancement</li>
      <li>Chemical Peels</li>
      <li>Facial Fillers</li>
      <li>Non Surgical Face Lift</li>
    </ul>
    <div class="contact">
      <p class="contact__label contact__label--phone">Phone</p>
      <p class="contact__phone">020 8794 2160</p>
      <p class="contact__label">Email</p>
      <p class="contact__email">pdabrackwellbookings@mailbox.co.uk</p>
      <p class="contact__label">Address</p>
      <p class="contact__address">52 Farrowmere Road<br>4 Brackwell High Street, Surrey, KT9 4WQ</p>
    </div>
  </section>

  <section class="card card--brand" aria-label="Brand side">
    <p class="website">www.penningtondoweaesthetics.co.uk</p>
    <div class="lips-photo" role="img" aria-label="Close-up photograph of glossy red lips"></div>
    <p class="brand-mark">PDA</p>
    <h1 class="brand-name">
      <span class="brand-name__first">Pennington Dowe</span><br>
      <span class="brand-name__second">Aesthetics</span>
    </h1>
  </section>

</body>
</html>
```